modern real estate design
business card/letterhead/envelop
Dorian Parks
President
408 W Birch Avenue Belle Plaine, MN 56093
dorian@tidewaterhomesgroup.com
www.tidewaterhomesgroup.com
Licensed Realtor with Quiet Harbor Real Estate
Escape Gravity.
newell343 newell343
I am also interested in getting a design done for metal business cards. It would be cool to have them die cut, etched, and have our two color logo on them. Thanks.

```html
<!DOCTYPE html>
<html lang="en">
<head>
<meta charset="utf-8">
<title>Tidewater Homes Group – Business Card</title>
<link href="https://fonts.googleapis.com/css2?family=Montserrat:wght@400;600;700&display=swap" rel="stylesheet">
<style>
  :root {
    --backdrop: #e9eaeb;
    --card: #ffffff;
    --teal: #2bb3c1;
    --ink: #4a4d50;
    --muted: #7b7f83;
  }
  * { margin: 0; padding: 0; box-sizing: border-box; }
  html, body { width: 1200px; height: 906px; overflow: hidden; }
  body {
    background: var(--backdrop);
    font-family: "Montserrat", Arial, sans-serif;
    color: var(--ink);
    position: relative;
  }
  .card {
    position: absolute;
    width: 525px;
    height: 300px;
    background: var(--card);
    box-shadow: 0 2px 6px rgba(0,0,0,0.08);
  }
  .card-back { left: 50px; top: 303px; }
  .card-front { left: 625px; top: 303px; }

  .brand {
    position: absolute;
    left: 50%;
    display: flex;
    align-items: center;
    gap: 10px;
    white-space: nowrap;
  }
  .brand-dot {
    flex: none;
    width: 12px; height: 12px;
    border-radius: 50%;
    background: var(--teal);
  }
  .brand-name {
    font-weight: 700;
    font-size: 19px;
    letter-spacing: 1.5px;
    text-transform: uppercase;
    color: var(--ink);
    white-space: nowrap;
  }
  .card-front .brand {
    top: 50%;
    transform: translate(-50%, -50%);
  }
  .card-front .brand-name { font-size: 22px; }
  .card-front .brand-dot { width: 14px; height: 14px; }

  .card-back .brand {
    top: 104px;
    transform: translateX(-50%);
  }
  .holder {
    position: absolute;
    left: 0; right: 0; top: 142px;
    text-align: center;
    white-space: nowrap;
  }
  .holder-name {
    font-weight: 600;
    font-size: 14px;
    letter-spacing: 1px;
    text-transform: uppercase;
  }
  .holder-title {
    font-size: 9px;
    letter-spacing: 1px;
    text-transform: uppercase;
    color: var(--muted);
    margin-top: 3px;
  }
  .contact-list {
    position: absolute;
    list-style: none;
    font-size: 9px;
    color: var(--muted);
    white-space: nowrap;
  }
  .contact-list li {
    display: flex;
    align-items: center;
    gap: 7px;
    height: 17px;
  }
  .contact-top { left: 26px; top: 28px; }
  .contact-bottom { right: 26px; bottom: 28px; }
  .icon {
    width: 12px; height: 12px;
    background: var(--teal);
    display: flex; align-items: center; justify-content: center;
    flex: none;
  }
  .icon svg { width: 8px; height: 8px; }
</style>
</head>
<body>
  <section class="card card-back">
    <ul class="contact-list contact-top">
      <li><span class="icon"><svg viewBox="0 0 10 10"><path d="M5 1a3 3 0 0 1 3 3c0 2-3 5-3 5S2 6 2 4a3 3 0 0 1 3-3z" fill="#fff"/></svg></span>408 W Birch Avenue</li>
      <li><span class="icon"><svg viewBox="0 0 10 10"><path d="M2 1h2l1 2-1 1c.5 1 1 1.5 2 2l1-1 2 1v2c-4 0-7-3-7-7z" fill="#fff"/></svg></span>507-555-0148</li>
      <li><span class="icon"><svg viewBox="0 0 10 10"><path d="M5 1a3 3 0 0 1 3 3c0 2-3 5-3 5S2 6 2 4a3 3 0 0 1 3-3z" fill="#fff"/></svg></span>Belle Plaine, MN 56093</li>
    </ul>

    <div class="brand">
      <span class="brand-dot"></span>
      <span class="brand-name">Tidewater Homes Group</span>
    </div>

    <div class="holder">
      <p class="holder-name">Dorian Parks</p>
      <p class="holder-title">President</p>
    </div>

    <ul class="contact-list contact-bottom">
      <li><span class="icon"><svg viewBox="0 0 10 10"><rect x="1" y="2.5" width="8" height="5" fill="none" stroke="#fff"/><path d="M1 2.5l4 3 4-3" fill="none" stroke="#fff"/></svg></span>dorian@tidewaterhomesgroup.com</li>
      <li><span class="icon"><svg viewBox="0 0 10 10"><circle cx="5" cy="5" r="3.5" fill="none" stroke="#fff"/><path d="M1.5 5h7M5 1.5v7" stroke="#fff"/></svg></span>www.tidewaterhomesgroup.com</li>
      <li><span class="icon"><svg viewBox="0 0 10 10"><path d="M2 8l3-6 3 6z" fill="#fff"/></svg></span>Quiet Harbor Real Estate</li>
    </ul>
  </section>

  <section class="card card-front">
    <div class="brand">
      <span class="brand-dot"></span>
      <span class="brand-name">Tidewater Homes Group</span>
    </div>
  </section>
</body>
</html>
```